New Frozen Vegetable Packaging for Retail

Hi all and welcome to our project! Looking for a versatile, enticing graphic design for our new frozen vegetable range packed in 250g bags sold at our grocery store.

We are a business located in Papua New Guinea and we manufacture and produce goods and have retail stores and restaurants. Our brand name for this product is ‘Brava Crisp’.

Target Audience: Our customers respond well to visual images rather than reading information, so keep it simple, bold and attractive! Our focus is - value for money.

Requirements:

• 1 x design so that we can easily change the description to fit multiple different products e.g. Mixed Vegetables / Frozen Peas / Frozen Corn
• Descriptions
o Mixed Vegetables (Product)
o Kwikim Friz to Preserve Freshness
o No Preservatives
o No Added Sugar
o No Artificial Colours or Flavours
o 250g NET

• Must have a clear window area for customers to see into the bag and visualise the product – would like around 20% of the bag to be clear.
• Our Brava Crisp Logo.
• An area for a barcode.
• Front and Back design.
• Require to be fully editable in either AI/PSD format.

No die line – please create the graphic for L20cm x W15cm with 1cm bleed (we will amend it to suit the products).

Thank you and look forward to collaborating on some great designs here :)

Target Market(s)

Budget, local Papua New Guinea customers

Industry/Entity Type

Retail Grocery

Font styles to use
Sans Serif

Requirements
Must have
• Generalised design to be adaptable to different products, logo, description, visual aids, window to see the product, barcode

```html
<!DOCTYPE html>
<html lang="en">
<head>
<meta charset="utf-8">
<title>Brava Crisp Mixed Vegetables – Front Panel</title>
<link href="https://fonts.googleapis.com/css2?family=Poppins:wght@400;500;700;800&family=Damion&display=swap" rel="stylesheet">
<style>
  :root{
    --backdrop:#d9dcdf;
    --film:#e4e6e8;
    --film-dark:#b9bcbf;
    --brand-red:#c0141c;
    --leaf:#3a9a2e;
    --leaf-deep:#2b8a22;
    --leaf-light:#86cc3c;
    --leaf-soft:#5cb543;
    --white:#ffffff;
  }
  *{margin:0;padding:0;box-sizing:border-box}
  html,body{width:1200px;height:1200px;overflow:hidden}
  body{background:var(--backdrop);font-family:"Poppins",sans-serif;position:relative}

  .pack{position:absolute;left:180px;top:160px;width:840px;height:880px;overflow:hidden;background:var(--film)}
  .pack__shapes{position:absolute;inset:0}

  .brand{position:absolute;top:110px;left:0;width:100%;display:flex;justify-content:center;align-items:center;gap:16px}
  .brand__mark{width:34px;height:34px;background:var(--brand-red)}
  .brand__name{font-weight:700;font-size:60px;color:var(--brand-red);letter-spacing:1px}

  .product{position:absolute;left:0;width:100%;text-align:center}
  .product__kind{top:268px;font-weight:800;font-size:64px;letter-spacing:3px;color:var(--white);
    -webkit-text-stroke:7px var(--leaf);paint-order:stroke fill}
  .product__name{top:318px;font-family:"Damion",cursive;font-size:104px;color:var(--white);
    -webkit-text-stroke:9px var(--leaf);paint-order:stroke fill;line-height:1.2}

  .claims{position:absolute;top:690px;left:110px;display:flex;gap:36px}
  .claim{width:88px;height:88px;border:3px solid var(--white);border-radius:50%;display:flex;align-items:center;justify-content:center;text-align:center;
    color:var(--white);font-weight:700;font-size:9.5px;line-height:1.25;padding:8px;text-transform:uppercase}

  .tagline{position:absolute;top:810px;left:110px;color:#e7f3df;font-size:19px;font-weight:500}
  .net{position:absolute;top:800px;right:120px;color:var(--white);font-size:24px;font-weight:700}
</style>
</head>
<body>
<main class="pack">
  <svg class="pack__shapes" viewBox="0 0 840 880" width="840" height="880" aria-hidden="false">
    <defs>
      <linearGradient id="fieldTone" x1="0" y1="0" x2="0" y2="1">
        <stop offset="0" stop-color="#eceeef"/>
        <stop offset="0.55" stop-color="#c9cbcd"/>
        <stop offset="1" stop-color="#9c9ea0"/>
      </linearGradient>
      <linearGradient id="vegTone" x1="0" y1="0" x2="1" y2="1">
        <stop offset="0" stop-color="#e58a5f"/>
        <stop offset="0.35" stop-color="#9fca86"/>
        <stop offset="0.6" stop-color="#e3cf56"/>
        <stop offset="1" stop-color="#e48a62"/>
      </linearGradient>
      <linearGradient id="leafTone" x1="0" y1="0" x2="0" y2="1">
        <stop offset="0" stop-color="#49a834"/>
        <stop offset="1" stop-color="#2e8f26"/>
      </linearGradient>
    </defs>
    <rect class="field-photo" x="0" y="0" width="840" height="440" fill="url(#fieldTone)" role="img" aria-label="Black and white photo of a farm field under a cloudy sky"/>
    <polygon class="window-band" points="0,425 840,408 840,428 0,445" fill="var(--leaf-light)"/>
    <polygon class="window-band" points="0,432 840,415 840,422 0,440" fill="var(--leaf-soft)"/>
    <polygon class="product-window" points="0,440 840,423 840,622 380,660 0,628" fill="url(#vegTone)" role="img" aria-label="Clear window showing frozen carrots, peas, corn and green beans"/>
    <polygon class="window-band" points="0,628 380,660 840,622 840,880 0,880" fill="var(--leaf-light)"/>
    <polygon class="base-panel" points="0,642 380,675 840,636 840,880 0,880" fill="url(#leafTone)"/>
  </svg>

  <header class="brand">
    <span class="brand__mark"></span>
    <span class="brand__name">Brava Crisp</span>
  </header>

  <h1 class="product product__kind">MIXED</h1>
  <h2 class="product product__name">Vegetables</h2>

  <ul class="claims">
    <li class="claim">No Artificial Colours or Flavours</li>
    <li class="claim">No Preser&shy;vatives</li>
    <li class="claim">No Added Sugar</li>
  </ul>

  <p class="tagline">Kwikim Friz to Preserve Freshness</p>
  <p class="net">250g NET</p>
</main>
</body>
</html>
```